Business Card, T Shirt ,Fax cover, Letterhead, Invoice
Kovac Painting & Decorating
Professional
Tobias Kovac
Bay no 482, 67 North Amber Way SW
California AB T3K5M8
tobias@kovacpaintworx.com
www.kovacpaintworx.com
Contents of the Invoice

```html
<!DOCTYPE html>
<html lang="en">
<head>
<meta charset="utf-8">
<title>Kovac Painting &amp; Decorating – Stationery</title>
<link href="https://fonts.googleapis.com/css2?family=Arimo:wght@400;700&display=swap" rel="stylesheet">
<style>
  :root{
    --backdrop:#c8c8c8;
    --paper:#ffffff;
    --card-dark:#333333;
    --brand-green:#6aa830;
    --ink:#555555;
    --ink-light:#888888;
    --fold:#cfcfcf;
  }
  *{box-sizing:border-box;margin:0;padding:0}
  html,body{width:1200px;height:655px;overflow:hidden}
  body{background:var(--backdrop);font-family:"Arimo",Arial,sans-serif;position:relative;color:var(--ink)}
  .sheet{position:absolute;background:var(--paper);box-shadow:0 1px 3px rgba(0,0,0,.25)}
  .brand{position:absolute;display:flex;align-items:center;gap:8px}
  .brand-dot{border-radius:50%;background:var(--brand-green);flex:none}
  .brand-name{color:var(--brand-green);font-weight:700;line-height:1.1}
  .contact{position:absolute;display:grid;grid-template-columns:auto auto;column-gap:14px;font-size:5.5px;line-height:1.6;color:var(--ink)}
  .web{position:absolute;font-size:6px;color:var(--brand-green)}

  /* letterhead */
  .letterhead{left:194px;top:17px;width:449px;height:621px}
  .letterhead .brand{left:28px;top:36px}
  .letterhead .brand-dot{width:28px;height:28px}
  .letterhead .brand-name{font-size:15px;width:140px}
  .letterhead .contact{left:266px;top:40px}
  .letterhead .web{right:22px;bottom:24px}

  /* business card front */
  .card-front{left:41px;top:209px;width:199px;height:110px;background:var(--card-dark)}
  .card-front .brand{left:26px;top:36px}
  .card-front .brand-dot{width:32px;height:32px}
  .card-front .brand-name{font-size:13px;width:120px}

  /* business card back */
  .card-back{left:41px;top:331px;width:199px;height:113px}
  .card-back .brand{left:10px;top:10px}
  .card-back .brand-dot{width:20px;height:20px}
  .card-back .brand-name{font-size:10px;width:110px}
  .card-back .web{left:10px;top:56px;font-size:5px;color:var(--ink)}
  .card-back .contact{left:10px;top:76px;font-size:4.5px;column-gap:16px}
  .card-back .holder{position:absolute;right:12px;bottom:18px;font-size:8px;color:var(--brand-green)}

  /* envelope back */
  .envelope-back{left:643px;top:79px;width:514px;height:235px}
  .envelope-back svg{position:absolute;inset:0}
  .envelope-back .brand-dot{position:absolute;left:237px;top:42px;width:40px;height:40px}

  /* envelope front */
  .envelope-front{left:643px;top:348px;width:514px;height:235px}
  .envelope-front .brand{left:42px;top:36px}
  .envelope-front .brand-dot{width:28px;height:28px}
  .envelope-front .brand-name{font-size:14px;width:150px}
  .envelope-front .contact{left:298px;top:40px}
  .envelope-front .web{left:42px;bottom:44px}
</style>
</head>
<body>

<section class="sheet letterhead" aria-label="Letterhead">
  <div class="brand"><span class="brand-dot"></span><span class="brand-name">Kovac Painting &amp; Decorating</span></div>
  <div class="contact">
    <span>Bay no 482, 67 North Amber Way SW</span><span>P: 403-555-0192</span>
    <span>California AB T3K5M8</span><span>F: 403-555-0147</span>
    <span>E: tobias@kovacpaintworx.com</span><span>C: 403-555-0168</span>
  </div>
  <div class="web">www.kovacpaintworx.com</div>
</section>

<section class="sheet card-front" aria-label="Business card front">
  <div class="brand"><span class="brand-dot"></span><span class="brand-name">Kovac Painting &amp; Decorating</span></div>
</section>

<section class="sheet card-back" aria-label="Business card back">
  <div class="brand"><span class="brand-dot"></span><span class="brand-name">Kovac Painting &amp; Decorating</span></div>
  <div class="web">www.kovacpaintworx.com</div>
  <div class="contact">
    <span>Bay no 482, 67 North Amber Way SW</span><span>P: 403-555-0192</span>
    <span>California AB T3K5M8</span><span>F: 403-555-0147</span>
    <span>tobias@kovacpaintworx.com</span><span>C: 403-555-0168</span>
  </div>
  <div class="holder">Tobias Kovac</div>
</section>

<section class="sheet envelope-back" aria-label="Envelope back">
  <svg width="514" height="235" viewBox="0 0 514 235">
    <polyline points="2,2 240,96 274,96 512,2" fill="none" stroke="var(--fold)" stroke-width="1.2"/>
    <line x1="2" y1="233" x2="200" y2="120" stroke="var(--fold)" stroke-width="1"/>
    <line x1="512" y1="233" x2="314" y2="120" stroke="var(--fold)" stroke-width="1"/>
  </svg>
  <span class="brand-dot"></span>
</section>

<section class="sheet envelope-front" aria-label="Envelope front">
  <div class="brand"><span class="brand-dot"></span><span class="brand-name">Kovac Painting &amp; Decorating</span></div>
  <div class="contact">
    <span>Bay no 482, 67 North Amber Way SW</span><span>P: 403-555-0192</span>
    <span>California AB T3K5M8</span><span>F: 403-555-0147</span>
    <span>E: tobias@kovacpaintworx.com</span><span>C: 403-555-0168</span>
  </div>
  <div class="web">www.kovacpaintworx.com</div>
</section>

</body>
</html>
```